Mental Health Nurse Wirrapunga Lands business card design

I need a modern looking business card that expresses my job out here in remote Western Australia with the Aboriginal people as a remote area nurse (RAN) specifically in Mental Health. The company I work for as aforementioned work solely with the Aboriginal communities in WA.
The colours of the company logo are orange and dark blue. Wirrapunga is pronounced in orange lettering along with health service in smaller lettering and aboriginal corporation like wise. I'm very flexible about the colour design as I am not to fond of it, however if we can keep close to the original as possible would be good. Perhaps a rounded corner would be good on the card, bottom right. Ultimately something related to the Aboriginal people, bright and modern and my job as a mental health remote area nurse.
Can you print and deliver these to me as I do not have the ability to print the finished product.

Target Market(s)

All People

Industry/Entity Type

Mental Health

Contact Information for Business Card

Gregory Latham
Wirrapunga Health Service, Aboriginal Corporation
RAN-Mental Health Coordinator
Mental Health Team
Ph 0491 563 804
email: glatham@wphealthsvc.org.au

Font styles to use
Sans Serif

Colors

Designer to choose colors to be used in the design.

Requirements
Must have
• A rounded lower right corner

```html
<!DOCTYPE html>
<html lang="en">
<head>
<meta charset="utf-8">
<title>Wirrapunga Health Service – Stationery</title>
<link rel="stylesheet" href="https://fonts.googleapis.com/css2?family=Marcellus+SC&family=Open+Sans:wght@400;600&display=swap">
<style>
  :root {
    --navy: #2b3f7e;
    --orange: #d9962c;
    --ink: #1e1e1e;
    --paper: #ffffff;
    --rule: #333333;
    --shadow: rgba(0, 0, 0, 0.35);
  }
  * { box-sizing: border-box; margin: 0; padding: 0; }
  html, body { width: 849px; height: 1200px; overflow: hidden; background: var(--paper); }
  .canvas { position: relative; width: 849px; height: 1200px; }

  .sheet {
    position: absolute;
    background: var(--paper);
    border: 1px solid #555;
    box-shadow: 8px 9px 10px var(--shadow);
    overflow: hidden;
  }

  .identity { position: absolute; display: flex; align-items: center; gap: 9px; }
  .identity__dot { width: 18px; height: 18px; border-radius: 50%; background: var(--orange); flex: none; }
  .identity__text {
    font-family: "Marcellus SC", serif;
    color: var(--navy);
    line-height: 1.25;
  }

  .role {
    font-family: "Open Sans", sans-serif;
    color: var(--ink);
    line-height: 1.3;
  }

  /* Letterhead */
  .letterhead { left: 40px; top: 160px; width: 592px; height: 904px; }
  .letterhead .identity { left: 38px; top: 30px; }
  .letterhead .identity__text { font-size: 11.5px; }
  .letterhead .role { position: absolute; left: 295px; top: 35px; font-size: 9px; }
  .letterhead__rule { position: absolute; left: 90px; top: 70px; width: 485px; border-top: 1px solid var(--rule); }
  .letterhead__footer { position: absolute; left: 0; bottom: 0; width: 100%; height: 44px; }

  /* Business card front */
  .card-front {
    left: 457px; top: 269px; width: 337px; height: 208px;
    background: var(--navy); border: none;
    border-bottom-right-radius: 22px;
  }
  .card-front .identity { left: 22px; top: 149px; }
  .card-front .identity__text { color: var(--paper); font-size: 15px; }

  /* Business card back */
  .card-back { left: 457px; top: 488px; width: 337px; height: 197px; border-bottom-right-radius: 22px; }
  .card-back .identity { left: 18px; top: 24px; }
  .card-back .identity__text { font-size: 11px; }
  .card-back .role { position: absolute; left: 0; top: 80px; width: 100%; text-align: center; font-size: 9.5px; }
  .card-back .contact {
    position: absolute; left: 0; top: 128px; width: 100%; text-align: center;
    font-family: "Open Sans", sans-serif; font-size: 5.5px; line-height: 1.4; color: var(--ink);
  }
  .card-back__footer { position: absolute; left: 0; bottom: 0; width: 100%; height: 60px; }

  /* Envelope */
  .envelope { left: 144px; top: 700px; width: 658px; height: 324px; }
  .envelope .identity { left: 28px; top: 22px; }
  .envelope .identity__text { font-size: 11.5px; }
  .envelope__stamp { position: absolute; right: 20px; top: 18px; width: 67px; height: 75px; border: 1px solid var(--rule); }
</style>
</head>
<body>
<main class="canvas">

  <section class="sheet letterhead" aria-label="Letterhead">
    <div class="identity">
      <span class="identity__dot"></span>
      <p class="identity__text">Gregory Latham<br>Wirrapunga Health Service</p>
    </div>
    <p class="role">Aboriginal Corporation<br>RAN-Mental Health<br>Coordinator Mental Health Team</p>
    <div class="letterhead__rule"></div>
    <svg class="letterhead__footer" viewBox="0 0 592 44" preserveAspectRatio="none">
      <path d="M0 2 C180 -2 400 6 592 16 L592 44 L0 44 Z" fill="var(--navy)"/>
      <path d="M0 8 C200 6 420 10 592 18 L592 30 L0 30 Z" fill="var(--paper)"/>
      <rect x="0" y="14" width="592" height="14" fill="var(--orange)"/>
    </svg>
  </section>

  <section class="sheet card-front" aria-label="Business card, front">
    <div class="identity">
      <p class="identity__text">Gregory Latham<br>Wirrapunga Health Service</p>
    </div>
  </section>

  <section class="sheet card-back" aria-label="Business card, back">
    <div class="identity">
      <span class="identity__dot"></span>
      <p class="identity__text">Gregory Latham<br>Wirrapunga Health Service</p>
    </div>
    <p class="role">Aboriginal Corporation<br>RAN-Mental Health<br>Coordinator Mental Health Team</p>
    <p class="contact">Ph 0491 563 804<br>email: glatham@wphealthsvc.org.au</p>
    <svg class="card-back__footer" viewBox="0 0 337 60" preserveAspectRatio="none">
      <path d="M0 60 L0 32 C120 30 260 14 337 0 L337 60 Z" fill="var(--navy)"/>
      <path d="M0 60 L0 38 C130 36 270 26 337 16 L337 60 Z" fill="var(--paper)"/>
      <path d="M0 60 L0 42 C130 40 270 34 337 28 L337 60 Z" fill="var(--orange)"/>
      <rect x="0" y="52" width="337" height="8" fill="var(--navy)"/>
    </svg>
  </section>

  <section class="sheet envelope" aria-label="Envelope">
    <div class="identity">
      <span class="identity__dot"></span>
      <p class="identity__text">Gregory Latham<br>Wirrapunga Health Service</p>
    </div>
    <div class="envelope__stamp"></div>
  </section>

</main>
</body>
</html>
```